International Trading Company, 'KIRO' needs a Business Card

The company name is "KIRO" and it has own logo design.
I'd like to use its logo on this business card.
I need two side Business Card.
I'll look forward to your great design.
Thank you very much in advance.

Contact Information for Business Card

Company Name : Kiro Harbour Limited
Information Example
Dorian Pallister
Mobile(use icon please) : 1 (212) 555-0143
Tel(use icon please) : 1 (212) 555-0178
Email(use icon please) : dorian27@kiroharbour-mail.com
Address(use icon please) : 482 Halden Ave, New York, NY 10160, USA

```html
<!DOCTYPE html>
<html lang="en">
<head>
<meta charset="utf-8">
<title>Kiro Harbour Limited – Business Card</title>
<link rel="stylesheet" href="https://fonts.googleapis.com/css2?family=Quicksand:wght@300;400&family=Roboto:wght@400&display=swap">
<style>
  :root {
    --charcoal: #414042;
    --mist: #e6e7e8;
    --white: #ffffff;
    --ink: #000000;
    --logo-grey: #9a9a9a;
    --card-text: #d6d6d6;
  }
  * { margin: 0; padding: 0; box-sizing: border-box; }
  html, body { width: 1200px; height: 794px; overflow: hidden; background: var(--white); }
  .sheet { position: relative; width: 1200px; height: 794px; background: var(--white); font-family: "Quicksand", sans-serif; }

  .card { position: absolute; width: 434px; height: 260px; background: var(--charcoal); }
  .card--front { left: 86px; top: 80px; display: flex; align-items: center; justify-content: center; }
  .card--back { left: 688px; top: 83px; color: var(--card-text); }

  .logo-name { font-family: "Quicksand", sans-serif; font-weight: 400; font-size: 104px; letter-spacing: 6px; color: var(--logo-grey); line-height: 1; }

  .company { position: absolute; top: 30px; left: 0; width: 100%; text-align: center; font-weight: 300; font-size: 31px; letter-spacing: 0.5px; }
  .person { position: absolute; top: 72px; left: 0; width: 100%; text-align: center; font-weight: 300; font-size: 24px; letter-spacing: 0.5px; }
  .contacts { position: absolute; left: 38px; top: 118px; list-style: none; }
  .contacts li { display: flex; align-items: center; height: 28.5px; font-weight: 300; font-size: 18.5px; }
  .contacts svg { width: 18px; height: 18px; margin-right: 4px; flex: none; stroke: var(--card-text); fill: none; stroke-width: 1.3; }

  .palette { position: absolute; left: 127px; top: 433px; display: flex; }
  .swatch { width: 64px; margin-right: 88px; text-align: center; }
  .swatch:nth-child(2) { margin-right: 71px; }
  .swatch-dot { width: 64px; height: 64px; border-radius: 50%; }
  .swatch-dot--charcoal { background: var(--charcoal); }
  .swatch-dot--mist { background: var(--mist); }
  .swatch-dot--white { background: var(--white); border: 1px solid var(--ink); }
  .swatch-code { display: block; margin-top: 20px; margin-left: -30px; width: 124px; font-family: "Roboto", sans-serif; font-size: 17px; color: var(--ink); }

  .typeface { position: absolute; left: 700px; top: 452px; width: 420px; text-align: center; font-weight: 300; font-size: 50px; color: var(--ink); }

  .footer-band { position: absolute; left: 0; top: 694px; width: 1200px; height: 54px; background: var(--ink); }
</style>
</head>
<body>
<main class="sheet">
  <section class="card card--front" aria-label="Card front">
    <span class="logo-name">KIRO</span>
  </section>

  <section class="card card--back" aria-label="Card back">
    <h1 class="company">Kiro Harbour Limited</h1>
    <p class="person">Dorian Pallister</p>
    <ul class="contacts">
      <li>
        <svg viewBox="0 0 18 18" aria-hidden="true"><rect x="5" y="1.5" width="8" height="15" rx="1.2"/><line x1="8" y1="14" x2="10" y2="14"/></svg>
        1 (212) 555-0143
      </li>
      <li>
        <svg viewBox="0 0 18 18" aria-hidden="true"><path d="M3 2.5l3 0 1.5 4-2 1.3a9 9 0 0 0 4.7 4.7l1.3-2 4 1.5v3a1.5 1.5 0 0 1-1.5 1.5A13 13 0 0 1 1.5 4 1.5 1.5 0 0 1 3 2.5z"/></svg>
        1 (212) 555-0178
      </li>
      <li>
        <svg viewBox="0 0 18 18" aria-hidden="true"><path d="M1.5 9L9 2.5 16.5 9"/><path d="M3.5 7.5V16h11V7.5"/><rect x="7.5" y="11" width="3" height="5"/></svg>
        482 Halden Ave, New York, NY 10160, USA
      </li>
      <li>
        <svg viewBox="0 0 18 18" aria-hidden="true"><rect x="1.5" y="4" width="15" height="10"/><path d="M1.5 4L9 10l7.5-6"/></svg>
        dorian27@kiroharbour-mail.com
      </li>
    </ul>
  </section>

  <section class="palette" aria-label="Colour palette">
    <div class="swatch"><div class="swatch-dot swatch-dot--charcoal"></div><span class="swatch-code">#414042</span></div>
    <div class="swatch"><div class="swatch-dot swatch-dot--mist"></div><span class="swatch-code">#e6e7e8</span></div>
    <div class="swatch"><div class="swatch-dot swatch-dot--white"></div><span class="swatch-code">#ffffff</span></div>
  </section>

  <p class="typeface">Velmora</p>

  <div class="footer-band" aria-hidden="true"></div>
</main>
</body>
</html>
```